Bravo Forge Business Card

We are a US manufacturer of RVL Shotgun Accessories along with some automotive accessories.
Our main business line is definitely the Shotgun Accessories.
Our company is the #1 Leader in RVL upgrade accessories in the United States.
We design, manufacture and retail all our products directly to the end user. We pride ourselves in superior quality and all manufactured in the USA.

On the card I want to convey made in the USA, Superior Quality and being the leader in RVL Accessories.
See our web site for a little information on our company. www.bravoforgeco.com

I would like it to have a picture of the RVL shotgun with all our accessories on it like the web site.
The Logo Shield should be a main focus as Branding is important. You can embelish the logo if you wish to make it more "Tactical" or updated looking. Try a few different versions.

Try to use some grey or Aluminum colors in the card. Since we machine metal to make all our products.
I'll send some images you can incorporate into the design.

Thank you.
Dean

Industry/Entity Type

Automotive

Contact Information for Business Card

Bravo Forge Creations Inc.
Dean Whitby
48 Pine Road, Mt.Vernon, NY 10557
www.BRAVOFORGECO.com
1(914)555-0173 (tel)

```html
<!DOCTYPE html>
<html lang="en">
<head>
<meta charset="utf-8">
<title>Bravo Forge Business Card</title>
<link href="https://fonts.googleapis.com/css2?family=Arimo:wght@400;700&display=swap" rel="stylesheet">
<style>
  :root {
    --stage: #e9e7e4;
    --card-white: #ffffff;
    --band-black: #000000;
    --band-grey: #9c9c9a;
    --strip-grey: #a9a9a9;
    --ink: #111111;
    --metal-light: #e4e4e4;
    --metal-mid: #b9b9b9;
    --metal-dark: #3a3a3a;
  }
  * { box-sizing: border-box; margin: 0; padding: 0; }
  html, body {
    width: 1200px; height: 848px; overflow: hidden;
    background: var(--stage);
    font-family: "Arimo", Helvetica, Arial, sans-serif;
  }
  .canvas {
    width: 1200px; height: 848px;
    display: flex; flex-direction: column; align-items: center; justify-content: center;
    gap: 36px;
  }
  .card {
    position: relative;
    width: 640px; height: 366px;
    background: var(--card-white);
    box-shadow: 0 6px 18px rgba(0,0,0,.18);
    overflow: hidden;
  }

  /* Front */
  .front__header {
    position: absolute; left: 0; top: 0; width: 100%; height: 74px;
    background: var(--band-black);
    display: flex; align-items: center; justify-content: center;
  }
  .front__company { color: #fff; font-size: 28px; font-weight: 400; letter-spacing: .2px; }
  .front__products {
    position: absolute; left: 232px; top: 86px; width: 176px; height: 112px;
    background: linear-gradient(160deg, var(--metal-light) 0%, var(--metal-mid) 55%, var(--metal-dark) 100%);
    border-radius: 4px;
  }
  .front__footer {
    position: absolute; left: 0; bottom: 0; width: 100%; height: 156px;
    background: var(--band-grey);
  }
  .contact {
    position: absolute; right: 20px; top: 12px;
    display: flex; flex-direction: column; gap: 3px;
  }
  .contact__row {
    display: flex; align-items: center; justify-content: flex-end; gap: 10px;
    font-size: 16px; color: var(--ink); line-height: 19px;
  }
  .contact__icon { width: 14px; height: 14px; flex: none; }
  .front__signature {
    position: absolute; left: 0; right: 20px; bottom: 22px;
    text-align: right;
    font-size: 25px; color: var(--ink); white-space: nowrap;
  }

  /* Back */
  .back__top-strip { position: absolute; left: 0; top: 0; width: 100%; height: 18px; background: var(--band-black); }
  .back__bottom-strip { position: absolute; left: 0; bottom: 0; width: 100%; height: 36px; background: var(--strip-grey); }
  .brand {
    position: absolute; left: 0; right: 0; top: 18px; bottom: 36px;
    display: flex; align-items: center; justify-content: center; gap: 18px;
    padding-bottom: 70px;
  }
  .brand__mark { width: 44px; height: 44px; background: var(--metal-dark); flex: none; }
  .brand__name { font-size: 46px; font-weight: 700; color: var(--metal-dark); letter-spacing: 1px; }
</style>
</head>
<body>
<main class="canvas">
  <section class="card card--front">
    <header class="front__header">
      <h1 class="front__company">Bravo Forge Creations Inc.</h1>
    </header>
    <div class="front__products" role="img" aria-label="Product photo: two hex keys, a black machined shotgun release lever and a brass-tipped screw"></div>
    <footer class="front__footer">
      <div class="contact">
        <p class="contact__row">1(914)555-0173
          <svg class="contact__icon" viewBox="0 0 16 16" aria-hidden="true"><path d="M3 2h3l1 3-2 1.5a9 9 0 0 0 4.5 4.5L11 9l3 1v3a1 1 0 0 1-1 1A12 12 0 0 1 2 3a1 1 0 0 1 1-1z" fill="#111"/></svg>
        </p>
        <p class="contact__row">www.BRAVOFORGECO.com
          <svg class="contact__icon" viewBox="0 0 16 16" aria-hidden="true"><circle cx="8" cy="8" r="7" fill="#111"/><path d="M1 8h14M8 1c-3 3-3 11 0 14M8 1c3 3 3 11 0 14" stroke="#9c9c9a" stroke-width="1.1" fill="none"/></svg>
        </p>
        <p class="contact__row">48 Pine Road, Mt.Vernon, NY 10557
          <svg class="contact__icon" viewBox="0 0 16 16" aria-hidden="true"><path d="M8 1a5 5 0 0 1 5 5c0 4-5 9-5 9S3 10 3 6a5 5 0 0 1 5-5z" fill="#111"/><circle cx="8" cy="6" r="1.8" fill="#9c9c9a"/></svg>
        </p>
      </div>
      <p class="front__signature">Dean Whitby 48 Pine Road, Mt.Vernon, NY 10557</p>
    </footer>
  </section>

  <section class="card card--back">
    <div class="back__top-strip"></div>
    <div class="brand">
      <span class="brand__mark"></span>
      <span class="brand__name">Bravo Forge</span>
    </div>
    <div class="back__bottom-strip"></div>
  </section>
</main>
</body>
</html>
```